KPRZ LLP - Web Design - 20th Anniversary

Create a web page and secondary page for a law firm. The firm is an IP or Patent Law Firm, look should be cutting edge. They are looking for a tech feel high end look. They want some callout to note their anniversary. Blue needs to be more impactful then current site. - See Brief Colors will be Blue and Gold as they currently are. Would like to see a home page and an attorney bio page and something that calls out the anniversary

Target Market(s)

Tech and Patent Companies - See Brief

Industry/Entity Type

Legal

Number of Pages Required

2 page

Colors
0054AA
0677BA
7BADD7
CADEEF
E8F1F8
FFF300
FFF600
FEFA6F
FFFEC7
FFFEE8

Requirements
Must have
• Impactful Blue, Tech and Cutting Edge Feel - See Brief
Nice to have
• Something noting the Anniversary, but not the basic ribbon - See Brief
Should not have
• Do not use any regular law firm images court room, court steps gavel NO ON THESE

```html
<!DOCTYPE html>
<html lang="en">
<head>
<meta charset="utf-8">
<title>KPRZ LLP — Professionals</title>
<link href="https://fonts.googleapis.com/css2?family=Roboto:wght@300;400;500;700;900&display=swap" rel="stylesheet">
<style>
:root{
  --blue:#0054AA;
  --blue-mid:#0677BA;
  --blue-light:#7BADD7;
  --blue-pale:#CADEEF;
  --blue-mist:#E8F1F8;
  --gold:#E3B81A;
  --gold-soft:#FEFA6F;
  --ink:#4a4a4a;
  --grey:#8a8a8a;
  --line:#dcdcdc;
  --white:#ffffff;
}
*{box-sizing:border-box;margin:0;padding:0}
html,body{width:1200px;height:3160px;overflow:hidden;background:var(--white);font-family:"Roboto",Arial,sans-serif;color:var(--ink)}
.page{position:relative;width:1200px;height:3160px}

.topbar{position:absolute;left:0;top:0;width:1200px;height:58px;background:var(--blue)}
.topbar .search{position:absolute;left:844px;top:12px}
.flag{position:absolute;top:15px;width:44px;height:30px;border:1px solid rgba(255,255,255,.5)}
.flag.us{left:894px;background:linear-gradient(180deg,#c8202e 0 14%,#fff 14% 28%,#c8202e 28% 42%,#fff 42% 56%,#c8202e 56% 70%,#fff 70% 84%,#c8202e 84%)}
.flag.us::before{content:"";position:absolute;left:0;top:0;width:20px;height:16px;background:#1f3a8a}
.flag.jp{left:957px;background:#fff}
.flag.jp::after{content:"";position:absolute;left:13px;top:6px;width:17px;height:17px;border-radius:50%;background:#d01c2c}
.flag.cn{left:1022px;background:#e0201c}

.nav{position:absolute;left:0;top:58px;width:1200px;height:100px;background:var(--white)}
.brand{position:absolute;left:118px;top:28px;display:flex;align-items:center;gap:14px}
.brand .mark{width:34px;height:44px;background:var(--blue)}
.brand .name{font-weight:500;font-size:40px;letter-spacing:1px;color:var(--blue)}
.menu{position:absolute;right:133px;top:40px;display:flex;gap:20px;list-style:none}
.menu li{font-size:16px;font-weight:500;color:var(--blue-light);position:relative}
.menu li.active{color:var(--blue)}
.menu li.active::after{content:"";position:absolute;left:50%;top:25px;width:4px;height:4px;margin-left:-2px;border-radius:50%;background:var(--gold)}

.hero{position:absolute;left:0;top:158px;width:1200px;height:551px;background:linear-gradient(120deg,#0a4fb0 0%,var(--blue) 60%,#0b5ab6 100%)}
.hero h1{position:absolute;left:134px;top:108px;font-weight:900;font-size:50px;line-height:60px;letter-spacing:1px;color:var(--white)}
.hero p{position:absolute;left:133px;top:357px;width:470px;font-size:16.5px;line-height:26px;color:var(--white)}
.badge{position:absolute;left:669px;top:44px;width:392px;height:385px;border-radius:50%;background:radial-gradient(circle at 50% 50%,#f1cf2a 0 32%,#d9a912 33% 40%,rgba(230,190,30,.35) 41% 62%,rgba(0,84,170,0) 70%)}

.stats{position:absolute;left:212px;top:628px;width:776px;height:151px;background:var(--white);border-radius:14px;box-shadow:0 4px 10px rgba(0,0,0,.18);display:flex}
.stat{flex:0 0 auto;text-align:center;border-right:1px solid #eee;padding-top:38px}
.stat:last-child{border-right:none}
.stat b{display:block;font-size:36px;font-weight:500;color:#333}
.stat span{display:block;margin-top:12px;font-size:17px;color:#666}

.section-title{position:absolute;left:0;top:826px;width:1200px;text-align:center;font-size:34px;font-weight:700;color:var(--blue)}

.team{position:absolute;left:132px;top:918px;width:937px}
.row{display:flex;gap:16px;margin-bottom:35px}
.row.last{margin-top:17px}
.member{position:relative;width:222px;height:315px}
.photo{position:absolute;left:51px;top:0;width:120px;height:138px;border-radius:0 0 60px 60px;overflow:hidden}
.photo::before{content:"";position:absolute;left:0;top:18px;width:120px;height:120px;border-radius:50%;background:var(--tone)}
.t1{--tone:radial-gradient(circle at 50% 40%,#e7c3a3 0 28%,#eef1f6 29%)}
.t2{--tone:radial-gradient(circle at 50% 35%,#d9a887 0 26%,#1e1e22 27%)}
.t3{--tone:radial-gradient(circle at 50% 35%,#b98466 0 26%,#2a1e22 27%)}
.t4{--tone:radial-gradient(circle at 50% 35%,#efd3b8 0 26%,#222 27%)}
.card{position:absolute;left:0;top:119px;width:222px;height:196px;border:1px solid #e3e3e3;border-radius:4px;background:var(--white);box-shadow:0 1px 4px rgba(0,0,0,.08);padding:0 17px}
.card h3{margin-top:27px;font-size:12.5px;font-weight:700;color:var(--blue);padding-bottom:5px;border-bottom:1px solid var(--line)}
.contact{list-style:none;margin-top:6px;padding-left:18px}
.contact li{display:flex;align-items:center;gap:10px;height:22px;font-size:9.5px;color:#666}
.contact svg{flex:0 0 auto}
.contact .sq{width:12px;height:12px;background:#8a8a8a}
.card p{margin-top:4px;font-size:8.6px;line-height:10px;color:#666}
.bio{display:block;margin:9px auto 0;width:59px;height:17px;border-radius:2px;background:var(--blue);color:var(--white);font-size:11px;font-weight:500;text-align:center;line-height:17px}

.footer{position:absolute;left:3px;top:2785px;width:1197px;height:375px;background:linear-gradient(120deg,#0a4fb0,var(--blue))}
.social{position:absolute;left:948px;top:36px;display:flex;gap:22px}
.social span{width:18px;height:18px;border-radius:50%;background:var(--blue-pale)}
.footer .rule{position:absolute;left:110px;width:979px;height:1px;background:rgba(255,255,255,.35)}
.f-brand{position:absolute;left:165px;top:106px;font-size:20px;font-weight:700;line-height:22px;color:var(--white);letter-spacing:.5px}
.office{position:absolute;left:183px;top:158px;font-size:13px;line-height:22px;color:var(--white)}
.office b{font-weight:500}
.office .tel{margin-top:22px}
.f-pin{position:absolute;left:145px;top:186px}
.f-phone{position:absolute;left:148px;top:269px}
.f-col{position:absolute;top:114px}
.f-col h4{font-size:19px;font-weight:500;color:var(--white);margin-bottom:18px}
.f-col ul{list-style:none}
.f-col li{font-size:13px;line-height:31px;color:var(--blue-pale)}
.copy{position:absolute;left:0;top:333px;width:1197px;text-align:center;font-size:13px;color:var(--blue-pale)}
</style>
</head>
<body>
<div class="page">

  <header class="topbar">
    <svg class="search" width="32" height="34" viewBox="0 0 32 34" fill="none" stroke="#CADEEF" stroke-width="2"><circle cx="13" cy="13" r="11"/><line x1="21" y1="21" x2="30" y2="32"/></svg>
    <span class="flag us" role="img" aria-label="English language flag"></span>
    <span class="flag jp" role="img" aria-label="Japanese language flag"></span>
    <span class="flag cn" role="img" aria-label="Chinese language flag"></span>
  </header>

  <nav class="nav">
    <div class="brand"><span class="mark"></span><span class="name">KPRZ LLP</span></div>
    <ul class="menu">
      <li>HOME</li><li>SERVICES</li><li>TECHNOLOGIES</li><li class="active">PROFESSIONALS</li><li>ABOUT US</li>
    </ul>
  </nav>

  <section class="hero">
    <h1>PATENT<br>TRADEMARK<br>DESIGN<br>COPYRIGHT</h1>
    <p>Serving Clients, Fortune 500 And Individual Inventors, Since 2003.</p>
    <div class="badge" role="img" aria-label="Gold laurel wreath anniversary emblem reading 20 years, crowned with three stars"></div>
  </section>

  <div class="stats">
    <div class="stat" style="width:184px"><b>18K</b><span>Total Patents</span></div>
    <div class="stat" style="width:203px"><b>1.5K</b><span>Clients</span></div>
    <div class="stat" style="width:202px"><b>20</b><span>Years In Services</span></div>
    <div class="stat" style="width:187px"><b>450</b><span>Excellent Review</span></div>
  </div>

  <h2 class="section-title">Professionals</h2>

  <main class="team">
    <!-- row template repeated -->
    <div class="row">
      <article class="member"><div class="photo t1" role="img" aria-label="Portrait of a smiling man in a white shirt"></div><div class="card"><h3>LOREM IPSUM</h3><ul class="contact"><li><svg width="14" height="11" viewBox="0 0 14 11" fill="none" stroke="#888"><rect x=".5" y=".5" width="13" height="10"/><path d="M.5 .5l6.5 6 6.5-6"/></svg>lorem@test.com</li><li><svg width="13" height="13" viewBox="0 0 13 13" fill="none" stroke="#888"><path d="M2 1l2.5 0 1 3-1.5 1a7 7 0 003.5 3.5l1-1.5 3 1v2.5a1 1 0 01-1 1A11 11 0 011 2a1 1 0 011-1z"/></svg>123-123-1234</li><li><span class="sq"></span>loremipsum</li></ul><p>Lorem Ipsum Dolor Sit Amet, Consectetur Adipiscing Elit, Sed Do Eiusmod Tempor Incididunt Ut Labore Et Dolore Magna Aliqua.</p><span class="bio">Bio</span></div></article>
      <article class="member"><div class="photo t2" role="img" aria-label="Portrait of a man in a dark suit"></div><div class="card"><h3>LOREM IPSUM</h3><ul class="contact"><li><svg width="14" height="11" viewBox="0 0 14 11" fill="none" stroke="#888"><rect x=".5" y=".5" width="13" height="10"/><path d="M.5 .5l6.5 6 6.5-6"/></svg>lorem@test.com</li><li><svg width="13" height="13" viewBox="0 0 13 13" fill="none" stroke="#888"><path d="M2 1l2.5 0 1 3-1.5 1a7 7 0 003.5 3.5l1-1.5 3 1v2.5a1 1 0 01-1 1A11 11 0 011 2a1 1 0 011-1z"/></svg>123-123-1234</li><li><span class="sq"></span>loremipsum</li></ul><p>Lorem Ipsum Dolor Sit Amet, Consectetur Adipiscing Elit, Sed Do Eiusmod Tempor Incididunt Ut Labore Et Dolore Magna Aliqua.</p><span class="bio">Bio</span></div></article>
      <article class="member"><div class="photo t3" role="img" aria-label="Portrait of a woman in a dark blazer"></div><div class="card"><h3>LOREM IPSUM</h3><ul class="contact"><li><svg width="14" height="11" viewBox="0 0 14 11" fill="none" stroke="#888"><rect x=".5" y=".5" width="13" height="10"/><path d="M.5 .5l6.5 6 6.5-6"/></svg>lorem@test.com</li><li><svg width="13" height="13" viewBox="0 0 13 13" fill="none" stroke="#888"><path d="M2 1l2.5 0 1 3-1.5 1a7 7 0 003.5 3.5l1-1.5 3 1v2.5a1 1 0 01-1 1A11 11 0 011 2a1 1 0 011-1z"/></svg>123-123-1234</li><li><span class="sq"></span>loremipsum</li></ul><p>Lorem Ipsum Dolor Sit Amet, Consectetur Adipiscing Elit, Sed Do Eiusmod Tempor Incididunt Ut Labore Et Dolore Magna Aliqua.</p><span class="bio">Bio</span></div></article>
      <article class="member"><div class="photo t4" role="img" aria-label="Portrait of a woman with glasses in a black suit"></div><div class="card"><h3>LOREM IPSUM</h3><ul class="contact"><li><svg width="14" height="11" viewBox="0 0 14 11" fill="none" stroke="#888"><rect x=".5" y=".5" width="13" height="10"/><path d="M.5 .5l6.5 6 6.5-6"/></svg>lorem@test.com</li><li><svg width="13" height="13" viewBox="0 0 13 13" fill="none" stroke="#888"><path d="M2 1l2.5 0 1 3-1.5 1a7 7 0 003.5 3.5l1-1.5 3 1v2.5a1 1 0 01-1 1A11 11 0 011 2a1 1 0 011-1z"/></svg>123-123-1234</li><li><span class="sq"></span>loremipsum</li></ul><p>Lorem Ipsum Dolor Sit Amet, Consectetur Adipiscing Elit, Sed Do Eiusmod Tempor Incididunt Ut Labore Et Dolore Magna Aliqua.</p><span class="bio">Bio</span></div></article>
    </div>
    <div class="row">
      <article class="member"><div class="photo t1" role="img" aria-label="Portrait of a smiling man in a white shirt"></div><div class="card"><h3>LOREM IPSUM</h3><ul class="contact"><li><svg width="14" height="11" viewBox="0 0 14 11" fill="none" stroke="#888"><rect x=".5" y=".5" width="13" height="10"/><path d="M.5 .5l6.5 6 6.5-6"/></svg>lorem@test.com</li><li><svg width="13" height="13" viewBox="0 0 13 13" fill="none" stroke="#888"><path d="M2 1l2.5 0 1 3-1.5 1a7 7 0 003.5 3.5l1-1.5 3 1v2.5a1 1 0 01-1 1A11 11 0 011 2a1 1 0 011-1z"/></svg>123-123-1234</li><li><span class="sq"></span>loremipsum</li></ul><p>Lorem Ipsum Dolor Sit Amet, Consectetur Adipiscing Elit, Sed Do Eiusmod Tempor Incididunt Ut Labore Et Dolore Magna Aliqua.</p><span class="bio">Bio</span></div></article>
      <article class="member"><div class="photo t2" role="img" aria-label="Portrait of a man in a dark suit"></div><div class="card"><h3>LOREM IPSUM</h3><ul class="contact"><li><svg width="14" height="11" viewBox="0 0 14 11" fill="none" stroke="#888"><rect x=".5" y=".5" width="13" height="10"/><path d="M.5 .5l6.5 6 6.5-6"/></svg>lorem@test.com</li><li><svg width="13" height="13" viewBox="0 0 13 13" fill="none" stroke="#888"><path d="M2 1l2.5 0 1 3-1.5 1a7 7 0 003.5 3.5l1-1.5 3 1v2.5a1 1 0 01-1 1A11 11 0 011 2a1 1 0 011-1z"/></svg>123-123-1234</li><li><span class="sq"></span>loremipsum</li></ul><p>Lorem Ipsum Dolor Sit Amet, Consectetur Adipiscing Elit, Sed Do Eiusmod Tempor Incididunt Ut Labore Et Dolore Magna Aliqua.</p><span class="bio">Bio</span></div></article>
      <article class="member"><div class="photo t3" role="img" aria-label="Portrait of a woman in a dark blazer"></div><div class="card"><h3>LOREM IPSUM</h3><ul class="contact"><li><svg width="14" height="11" viewBox="0 0 14 11" fill="none" stroke="#888"><rect x=".5" y=".5" width="13" height="10"/><path d="M.5 .5l6.5 6 6.5-6"/></svg>lorem@test.com</li><li><svg width="13" height="13" viewBox="0 0 13 13" fill="none" stroke="#888"><path d="M2 1l2.5 0 1 3-1.5 1a7 7 0 003.5 3.5l1-1.5 3 1v2.5a1 1 0 01-1 1A11 11 0 011 2a1 1 0 011-1z"/></svg>123-123-1234</li><li><span class="sq"></span>loremipsum</li></ul><p>Lorem Ipsum Dolor Sit Amet, Consectetur Adipiscing Elit, Sed Do Eiusmod Tempor Incididunt Ut Labore Et Dolore Magna Aliqua.</p><span class="bio">Bio</span></div></article>
      <article class="member"><div class="photo t4" role="img" aria-label="Portrait of a woman with glasses in a black suit"></div><div class="card"><h3>LOREM IPSUM</h3><ul class="contact"><li><svg width="14" height="11" viewBox="0 0 14 11" fill="none" stroke="#888"><rect x=".5" y=".5" width="13" height="10"/><path d="M.5 .5l6.5 6 6.5-6"/></svg>lorem@test.com</li><li><svg width="13" height="13" viewBox="0 0 13 13" fill="none" stroke="#888"><path d="M2 1l2.5 0 1 3-1.5 1a7 7 0 003.5 3.5l1-1.5 3 1v2.5a1 1 0 01-1 1A11 11 0 011 2a1 1 0 011-1z"/></svg>123-123-1234</li><li><span class="sq"></span>loremipsum</li></ul><p>Lorem Ipsum Dolor Sit Amet, Consectetur Adipiscing Elit, Sed Do Eiusmod Tempor Incididunt Ut Labore Et Dolore Magna Aliqua.</p><span class="bio">Bio</span></div></article>
    </div>
    <div class="row">
      <article class="member"><div class="photo t1" role="img" aria-label="Portrait of a smiling man in a white shirt"></div><div class="card"><h3>LOREM IPSUM</h3><ul class="contact"><li><svg width="14" height="11" viewBox="0 0 14 11" fill="none" stroke="#888"><rect x=".5" y=".5" width="13" height="10"/><path d="M.5 .5l6.5 6 6.5-6"/></svg>lorem@test.com</li><li><svg width="13" height="13" viewBox="0 0 13 13" fill="none" stroke="#888"><path d="M2 1l2.5 0 1 3-1.5 1a7 7 0 003.5 3.5l1-1.5 3 1v2.5a1 1 0 01-1 1A11 11 0 011 2a1 1 0 011-1z"/></svg>123-123-1234</li><li><span class="sq"></span>loremipsum</li></ul><p>Lorem Ipsum Dolor Sit Amet, Consectetur Adipiscing Elit, Sed Do Eiusmod Tempor Incididunt Ut Labore Et Dolore Magna Aliqua.</p><span class="bio">Bio</span></div></article>
      <article class="member"><div class="photo t2" role="img" aria-label="Portrait of a man in a dark suit"></div><div class="card"><h3>LOREM IPSUM</h3><ul class="contact"><li><svg width="14" height="11" viewBox="0 0 14 11" fill="none" stroke="#888"><rect x=".5" y=".5" width="13" height="10"/><path d="M.5 .5l6.5 6 6.5-6"/></svg>lorem@test.com</li><li><svg width="13" height="13" viewBox="0 0 13 13" fill="none" stroke="#888"><path d="M2 1l2.5 0 1 3-1.5 1a7 7 0 003.5 3.5l1-1.5 3 1v2.5a1 1 0 01-1 1A11 11 0 011 2a1 1 0 011-1z"/></svg>123-123-1234</li><li><span class="sq"></span>loremipsum</li></ul><p>Lorem Ipsum Dolor Sit Amet, Consectetur Adipiscing Elit, Sed Do Eiusmod Tempor Incididunt Ut Labore Et Dolore Magna Aliqua.</p><span class="bio">Bio</span></div></article>
      <article class="member"><div class="photo t3" role="img" aria-label="Portrait of a woman in a dark blazer"></div><div class="card"><h3>LOREM IPSUM</h3><ul class="contact"><li><svg width="14" height="11" viewBox="0 0 14 11" fill="none" stroke="#888"><rect x=".5" y=".5" width="13" height="10"/><path d="M.5 .5l6.5 6 6.5-6"/></svg>lorem@test.com</li><li><svg width="13" height="13" viewBox="0 0 13 13" fill="none" stroke="#888"><path d="M2 1l2.5 0 1 3-1.5 1a7 7 0 003.5 3.5l1-1.5 3 1v2.5a1 1 0 01-1 1A11 11 0 011 2a1 1 0 011-1z"/></svg>123-123-1234</li><li><span class="sq"></span>loremipsum</li></ul><p>Lorem Ipsum Dolor Sit Amet, Consectetur Adipiscing Elit, Sed Do Eiusmod Tempor Incididunt Ut Labore Et Dolore Magna Aliqua.</p><span class="bio">Bio</span></div></article>
      <article class="member"><div class="photo t4" role="img" aria-label="Portrait of a woman with glasses in a black suit"></div><div class="card"><h3>LOREM IPSUM</h3><ul class="contact"><li><svg width="14" height="11" viewBox="0 0 14 11" fill="none" stroke="#888"><rect x=".5" y=".5" width="13" height="10"/><path d="M.5 .5l6.5 6 6.5-6"/></svg>lorem@test.com</li><li><svg width="13" height="13" viewBox="0 0 13 13" fill="none" stroke="#888"><path d="M2 1l2.5 0 1 3-1.5 1a7 7 0 003.5 3.5l1-1.5 3 1v2.5a1 1 0 01-1 1A11 11 0 011 2a1 1 0 011-1z"/></svg>123-123-1234</li><li><span class="sq"></span>loremipsum</li></ul><p>Lorem Ipsum Dolor Sit Amet, Consectetur Adipiscing Elit, Sed Do Eiusmod Tempor Incididunt Ut Labore Et Dolore Magna Aliqua.</p><span class="bio">Bio</span></div></article>
    </div>
    <div class="row">
      <article class="member"><div class="photo t1" role="img" aria-label="Portrait of a smiling man in a white shirt"></div><div class="card"><h3>LOREM IPSUM</h3><ul class="contact"><li><svg width="14" height="11" viewBox="0 0 14 11" fill="none" stroke="#888"><rect x=".5" y=".5" width="13" height="10"/><path d="M.5 .5l6.5 6 6.5-6"/></svg>lorem@test.com</li><li><svg width="13" height="13" viewBox="0 0 13 13" fill="none" stroke="#888"><path d="M2 1l2.5 0 1 3-1.5 1a7 7 0 003.5 3.5l1-1.5 3 1v2.5a1 1 0 01-1 1A11 11 0 011 2a1 1 0 011-1z"/></svg>123-123-1234</li><li><span class="sq"></span>loremipsum</li></ul><p>Lorem Ipsum Dolor Sit Amet, Consectetur Adipiscing Elit, Sed Do Eiusmod Tempor Incididunt Ut Labore Et Dolore Magna Aliqua.</p><span class="bio">Bio</span></div></article>
      <article class="member"><div class="photo t2" role="img" aria-label="Portrait of a man in a dark suit"></div><div class="card"><h3>LOREM IPSUM</h3><ul class="contact"><li><svg width="14" height="11" viewBox="0 0 14 11" fill="none" stroke="#888"><rect x=".5" y=".5" width="13" height="10"/><path d="M.5 .5l6.5 6 6.5-6"/></svg>lorem@test.com</li><li><svg width="13" height="13" viewBox="0 0 13 13" fill="none" stroke="#888"><path d="M2 1l2.5 0 1 3-1.5 1a7 7 0 003.5 3.5l1-1.5 3 1v2.5a1 1 0 01-1 1A11 11 0 011 2a1 1 0 011-1z"/></svg>123-123-1234</li><li><span class="sq"></span>loremipsum</li></ul><p>Lorem Ipsum Dolor Sit Amet, Consectetur Adipiscing Elit, Sed Do Eiusmod Tempor Incididunt Ut Labore Et Dolore Magna Aliqua.</p><span class="bio">Bio</span></div></article>
      <article class="member"><div class="photo t3" role="img" aria-label="Portrait of a woman in a dark blazer"></div><div class="card"><h3>LOREM IPSUM</h3><ul class="contact"><li><svg width="14" height="11" viewBox="0 0 14 11" fill="none" stroke="#888"><rect x=".5" y=".5" width="13" height="10"/><path d="M.5 .5l6.5 6 6.5-6"/></svg>lorem@test.com</li><li><svg width="13" height="13" viewBox="0 0 13 13" fill="none" stroke="#888"><path d="M2 1l2.5 0 1 3-1.5 1a7 7 0 003.5 3.5l1-1.5 3 1v2.5a1 1 0 01-1 1A11 11 0 011 2a1 1 0 011-1z"/></svg>123-123-1234</li><li><span class="sq"></span>loremipsum</li></ul><p>Lorem Ipsum Dolor Sit Amet, Consectetur Adipiscing Elit, Sed Do Eiusmod Tempor Incididunt Ut Labore Et Dolore Magna Aliqua.</p><span class="bio">Bio</span></div></article>
      <article class="member"><div class="photo t4" role="img" aria-label="Portrait of a woman with glasses in a black suit"></div><div class="card"><h3>LOREM IPSUM</h3><ul class="contact"><li><svg width="14" height="11" viewBox="0 0 14 11" fill="none" stroke="#888"><rect x=".5" y=".5" width="13" height="10"/><path d="M.5 .5l6.5 6 6.5-6"/></svg>lorem@test.com</li><li><svg width="13" height="13" viewBox="0 0 13 13" fill="none" stroke="#888"><path d="M2 1l2.5 0 1 3-1.5 1a7 7 0 003.5 3.5l1-1.5 3 1v2.5a1 1 0 01-1 1A11 11 0 011 2a1 1 0 011-1z"/></svg>123-123-1234</li><li><span class="sq"></span>loremipsum</li></ul><p>Lorem Ipsum Dolor Sit Amet, Consectetur Adipiscing Elit, Sed Do Eiusmod Tempor Incididunt Ut Labore Et Dolore Magna Aliqua.</p><span class="bio">Bio</span></div></article>
    </div>
    <div class="row last">
      <article class="member"><div class="photo t1" role="img" aria-label="Portrait of a smiling man in a white shirt"></div><div class="card"><h3>LOREM IPSUM</h3><ul class="contact"><li><svg width="14" height="11" viewBox="0 0 14 11" fill="none" stroke="#888"><rect x=".5" y=".5" width="13" height="10"/><path d="M.5 .5l6.5 6 6.5-6"/></svg>lorem@test.com</li><li><svg width="13" height="13" viewBox="0 0 13 13" fill="none" stroke="#888"><path d="M2 1l2.5 0 1 3-1.5 1a7 7 0 003.5 3.5l1-1.5 3 1v2.5a1 1 0 01-1 1A11 11 0 011 2a1 1 0 011-1z"/></svg>123-123-1234</li><li><span class="sq"></span>loremipsum</li></ul><p>Lorem Ipsum Dolor Sit Amet, Consectetur Adipiscing Elit, Sed Do Eiusmod Tempor Incididunt Ut Labore Et Dolore Magna Aliqua.</p><span class="bio">Bio</span></div></article>
      <article class="member"><div class="photo t2" role="img" aria-label="Portrait of a man in a dark suit"></div><div class="card"><h3>LOREM IPSUM</h3><ul class="contact"><li><svg width="14" height="11" viewBox="0 0 14 11" fill="none" stroke="#888"><rect x=".5" y=".5" width="13" height="10"/><path d="M.5 .5l6.5 6 6.5-6"/></svg>lorem@test.com</li><li><svg width="13" height="13" viewBox="0 0 13 13" fill="none" stroke="#888"><path d="M2 1l2.5 0 1 3-1.5 1a7 7 0 003.5 3.5l1-1.5 3 1v2.5a1 1 0 01-1 1A11 11 0 011 2a1 1 0 011-1z"/></svg>123-123-1234</li><li><span class="sq"></span>loremipsum</li></ul><p>Lorem Ipsum Dolor Sit Amet, Consectetur Adipiscing Elit, Sed Do Eiusmod Tempor Incididunt Ut Labore Et Dolore Magna Aliqua.</p><span class="bio">Bio</span></div></article>
      <article class="member"><div class="photo t3" role="img" aria-label="Portrait of a woman in a dark blazer"></div><div class="card"><h3>LOREM IPSUM</h3><ul class="contact"><li><svg width="14" height="11" viewBox="0 0 14 11" fill="none" stroke="#888"><rect x=".5" y=".5" width="13" height="10"/><path d="M.5 .5l6.5 6 6.5-6"/></svg>lorem@test.com</li><li><svg width="13" height="13" viewBox="0 0 13 13" fill="none" stroke="#888"><path d="M2 1l2.5 0 1 3-1.5 1a7 7 0 003.5 3.5l1-1.5 3 1v2.5a1 1 0 01-1 1A11 11 0 011 2a1 1 0 011-1z"/></svg>123-123-1234</li><li><span class="sq"></span>loremipsum</li></ul><p>Lorem Ipsum Dolor Sit Amet, Consectetur Adipiscing Elit, Sed Do Eiusmod Tempor Incididunt Ut Labore Et Dolore Magna Aliqua.</p><span class="bio">Bio</span></div></article>
      <article class="member"><div class="photo t4" role="img" aria-label="Portrait of a woman with glasses in a black suit"></div><div class="card"><h3>LOREM IPSUM</h3><ul class="contact"><li><svg width="14" height="11" viewBox="0 0 14 11" fill="none" stroke="#888"><rect x=".5" y=".5" width="13" height="10"/><path d="M.5 .5l6.5 6 6.5-6"/></svg>lorem@test.com</li><li><svg width="13" height="13" viewBox="0 0 13 13" fill="none" stroke="#888"><path d="M2 1l2.5 0 1 3-1.5 1a7 7 0 003.5 3.5l1-1.5 3 1v2.5a1 1 0 01-1 1A11 11 0 011 2a1 1 0 011-1z"/></svg>123-123-1234</li><li><span class="sq"></span>loremipsum</li></ul><p>Lorem Ipsum Dolor Sit Amet, Consectetur Adipiscing Elit, Sed Do Eiusmod Tempor Incididunt Ut Labore Et Dolore Magna Aliqua.</p><span class="bio">Bio</span></div></article>
    </div>
  </main>

  <footer class="footer">
    <div class="social"><span></span><span></span><span></span><span></span></div>
    <div class="rule" style="top:82px"></div>
    <div class="f-brand">KPRZ LLP</div>
    <svg class="f-pin" width="30" height="40" viewBox="0 0 30 40"><path d="M15 1a13 13 0 0113 13c0 10-13 25-13 25S2 24 2 14A13 13 0 0115 1z" fill="#fff"/><circle cx="15" cy="14" r="5" fill="#0054AA"/></svg>
    <svg class="f-phone" width="26" height="28" viewBox="0 0 26 28" fill="none" stroke="#fff" stroke-width="1.5"><path d="M4 2l5 0 2 6-3 2a14 14 0 007 8l2-3 6 2v5a2 2 0 01-2 2A22 22 0 012 4a2 2 0 012-2z"/></svg>
    <div class="office">
      <b>Main Office</b><br>4120 Meridian Way<br>Suite 300<br>Fairbrook, VA 22090
      <div class="tel">Tel: 555-014-2200<br>Fax: 555-019-4410</div>
    </div>
    <div class="f-col" style="left:434px"><h4>Quick Links</h4><ul><li>Services</li><li>Technologies</li><li>Professionals</li><li>CAFC Alerts</li></ul></div>
    <div class="f-col" style="left:683px"><h4>About</h4><ul><li>Offices</li><li>Careers</li><li>Firm History</li><li>Contacts</li><li>News And Publications</li></ul></div>
    <div class="f-col" style="left:961px"><h4>Resources</h4><ul><li>Forms</li><li>Materials</li><li>News And Events</li><li>Locations</li></ul></div>
    <div class="rule" style="top:322px"></div>
    <div class="copy">Copyright©Test. All Right Reserved</div>
  </footer>

</div>
</body>
</html>
```